Remote Computer Support PostCard

We need a Postcard Ad for marketing to businesses that need Remote Computer Support and Security. 2 sided and able to be mailed. Can be any color but color we use mostly is red. Remote Computer Support and Security per PC. Includes Remote Monitoring and Maintenance(RMM) Agent, Business Security Tools including Antivirus, Anti Malware, Ransomware Protection, Intrusion Prevention, Content Filtering and others. All remote support you need for $69.99 per pc per month.

Target Market(s)

All Businesses

Industry/Entity Type

Computer Support for Businesses

Colors
EB3D1F
EC4F4E
F09395
F8D3D4
FCEDEE

Requirements
Must have
• Bytharo, Inc. (555) 314-2968 . Sales@bytharo-example.com. Designed to be mailed. 6x9 Postcard Mailer Size Final 6.25" x 9" Ink & Bleed Four Color Process, Full Bleed Two Sides. Must have places for postage.
Nice to have
• Main lines should be in top 1/3 of postcard to stand out in mail.

```html
<!DOCTYPE html>
<html lang="en">
<head>
<meta charset="utf-8">
<title>Bytharo Remote Support Postcard</title>
<link href="https://fonts.googleapis.com/css2?family=Anton&family=Montserrat:wght@500;600;700;800&display=swap" rel="stylesheet">
<style>
  :root {
    --red: #d21f26;
    --red-dark: #9e1a1f;
    --navy: #1c2a78;
    --navy-deep: #0f1a52;
    --blue: #3346b0;
    --yellow: #ffe600;
    --black: #0b0b0b;
    --white: #ffffff;
    --stamp: #8c8f96;
    --backdrop: #b4b4b4;
    --ink: #111111;
  }
  * { box-sizing: border-box; margin: 0; padding: 0; }
  html, body { width: 1200px; height: 1117px; overflow: hidden; }
  body {
    background: var(--backdrop);
    font-family: "Montserrat", sans-serif;
    position: relative;
  }
  .postcard {
    position: absolute;
    width: 720px;
    height: 500px;
    overflow: hidden;
    background: var(--white);
    box-shadow: 0 10px 28px rgba(0,0,0,.3);
  }
  .postcard--front { left: 40px; top: 40px; }
  .postcard--back { left: 440px; top: 577px; }
  .postcard svg.backdrop { position: absolute; inset: 0; }
  .abs { position: absolute; }

  /* front */
  .brand-name {
    font-family: "Montserrat", sans-serif;
    font-weight: 800;
    color: var(--white);
  }
  .front-brand { left: 420px; top: 95px; font-size: 50px; letter-spacing: .5px; }
  .front-headline {
    left: 0; width: 720px; top: 226px;
    text-align: center;
    font-family: "Anton", sans-serif;
    font-weight: 400;
    color: var(--white);
    font-size: 36px;
    line-height: 42px;
    padding-left: 40px;
  }
  .highlight { color: var(--yellow); }
  .price-box {
    left: 40px; top: 324px; width: 310px; height: 160px;
    background: var(--white);
    border-radius: 16px;
    border: 3px solid var(--red);
    box-shadow: 0 0 0 4px var(--white), 0 4px 10px rgba(0,0,0,.35);
    padding: 32px 14px 0 18px;
  }
  .price-tab {
    left: 80px; top: -3px;
    background: var(--red-dark);
    color: var(--white);
    font-weight: 800;
    font-size: 15px;
    padding: 5px 22px 6px;
    border-radius: 0 0 12px 12px;
  }
  .price-figure {
    color: var(--red);
    font-weight: 800;
    font-size: 58px;
    line-height: 60px;
    letter-spacing: -1px;
  }
  .price-unit { font-size: 12px; letter-spacing: 0; vertical-align: 34px; margin-left: 4px; }
  .price-note {
    margin-top: 8px;
    font-size: 10px;
    font-weight: 700;
    line-height: 12.5px;
    color: var(--ink);
    text-transform: uppercase;
  }
  .feature-list {
    left: 395px; top: 318px; width: 300px;
    list-style: none;
    color: var(--white);
    font-weight: 600;
    font-size: 13px;
    line-height: 22px;
    text-transform: uppercase;
  }
  .tick-list li { position: relative; padding-left: 22px; }
  .tick-list li::before {
    content: "";
    position: absolute; left: 2px; top: 6px;
    width: 6px; height: 10px;
    border: solid var(--yellow);
    border-width: 0 3px 3px 0;
    transform: rotate(40deg);
  }

  /* back */
  .stamp-box { right: 22px; top: 22px; width: 70px; height: 76px; background: var(--stamp); }
  .back-headline {
    left: 38px; top: 40px;
    font-family: "Anton", sans-serif;
    font-weight: 400;
    font-size: 32px;
    color: var(--white);
  }
  .back-headline .first { border-bottom: 2px solid var(--white); padding-bottom: 2px; }
  .remote-points {
    left: 40px; top: 96px; width: 270px;
    list-style: none;
    color: var(--white);
    font-size: 11px;
    font-weight: 500;
    line-height: 14px;
  }
  .remote-points li { margin-bottom: 3px; }
  .remote-points li::before { border-color: var(--white); top: 3px; width: 5px; height: 9px; border-width: 0 2px 2px 0; }
  .offer { left: 60px; top: 212px; }
  .offer-line { font-weight: 800; font-size: 15px; color: var(--ink); line-height: 18px; }
  .offer-line--accent { color: var(--red); }
  .includes-title { margin-top: 6px; font-weight: 800; font-size: 14px; line-height: 17px; color: var(--ink); }
  .includes-list { list-style: none; font-size: 11px; font-weight: 500; line-height: 13px; color: var(--ink); }
  .includes-list li::before { content: "• "; }
  .security-panel {
    left: 0; top: 318px; width: 400px; height: 182px;
    background: var(--black);
    border-top-right-radius: 42px;
  }
  .security-columns { left: 40px; top: 330px; display: flex; gap: 20px; }
  .security-columns ul {
    list-style: none;
    color: var(--white);
    font-size: 9.5px;
    font-weight: 600;
    line-height: 11px;
    white-space: nowrap;
  }
  .security-columns li { padding-left: 15px; }
  .security-columns li::before { top: 1px; left: 1px; width: 4px; height: 8px; border-width: 0 2px 2px 0; }
  .contact { left: 48px; top: 448px; color: var(--white); }
  .contact-phone { display: flex; align-items: center; gap: 8px; font-weight: 700; font-size: 22px; line-height: 26px; }
  .contact-email { font-size: 12px; line-height: 15px; font-weight: 500; margin-left: 34px; }
  .back-brand { right: 36px; bottom: 78px; font-size: 42px; color: var(--ink); }
</style>
</head>
<body>

<section class="postcard postcard--front" aria-label="Postcard front">
  <svg class="backdrop" width="720" height="500" viewBox="0 0 720 500">
    <defs>
      <linearGradient id="navyFade" x1="0" y1="0" x2="1" y2="1">
        <stop offset="0" stop-color="#263a9a"/>
        <stop offset="1" stop-color="#0f1a52"/>
      </linearGradient>
      <linearGradient id="photoTone" x1="0" y1="0" x2="1" y2="1">
        <stop offset="0" stop-color="#2a3448"/>
        <stop offset=".6" stop-color="#5a5560"/>
        <stop offset="1" stop-color="#c9a68a"/>
      </linearGradient>
    </defs>
    <rect width="720" height="500" fill="url(#navyFade)"/>
    <path role="img" aria-label="Photo: business people at a laptop with a glowing security shield overlay" d="M0 0 H330 C390 70 400 170 370 250 L0 360 Z" fill="url(#photoTone)"/>
    <path d="M0 330 C170 170 470 150 720 205 V500 H0 Z" fill="var(--blue)"/>
    <path d="M0 348 C170 195 470 175 720 228 V500 H0 Z" fill="var(--white)"/>
    <path d="M0 358 C170 205 470 185 720 238 V500 H0 Z" fill="var(--red)"/>
    <path d="M370 350 C480 310 600 295 720 292 V500 H300 Z" fill="var(--black)"/>
  </svg>
  <div class="abs brand-name front-brand">Bytharo</div>
  <h1 class="abs front-headline">Finaly Computer<br>Security and Support <span class="highlight">made Easy!</span></h1>
  <div class="abs price-box">
    <div class="abs price-tab">FOR ONLY</div>
    <div class="price-figure">$69.99/<span class="price-unit">MONTH</span></div>
    <p class="price-note">Per PC you can get world class security services and unlimited remote technical support.</p>
  </div>
  <ul class="abs feature-list tick-list">
    <li>Automated Desktop OS Updates</li>
    <li>Automated System Cleanup</li>
    <li>Monthly Reports</li>
    <li>Managed Antivirus including ransomware detection and protection</li>
  </ul>
</section>

<section class="postcard postcard--back" aria-label="Postcard back">
  <svg class="backdrop" width="720" height="500" viewBox="0 0 720 500">
    <path d="M0 0 H500 C450 120 320 190 0 205 Z" fill="var(--red)"/>
    <path d="M0 425 C160 385 330 395 520 500 H0 Z" fill="var(--red)"/>
    <path d="M0 442 C160 404 320 414 490 500 H0 Z" fill="var(--black)"/>
  </svg>
  <div class="abs security-panel"></div>
  <div class="abs stamp-box" aria-label="Postage area"></div>
  <h2 class="abs back-headline"><span class="first">AUTOMATED</span> <span class="highlight">REMOTE SUPPORT</span></h2>
  <ul class="abs remote-points tick-list">
    <li>Remote monitoring and maintenance tools monitor your devices in real-time.</li>
    <li>Instantly informing you of current issues and flagging potential problems.</li>
  </ul>
  <div class="abs offer">
    <p class="offer-line">ONE TIME SETUP FEE OF $69.99 THEN</p>
    <p class="offer-line offer-line--accent">ONLY $69.99 PER MONTH PER PC</p>
    <p class="includes-title">Includes:</p>
    <ul class="includes-list">
      <li>Remote Monitoring and Management Agent (RMM)</li>
      <li>Help Desk Application on Desktop</li>
      <li>NovaShield Business Security</li>
    </ul>
  </div>
  <div class="abs security-columns">
    <ul class="tick-list">
      <li>ANTIVIRUS</li>
      <li>Real-Time Scan</li>
      <li>Scheduled Scan</li>
      <li>Manual Scan</li>
      <li>Behavior Monitoring</li>
      <li>Malware Behavior Blocking</li>
      <li>Ransomware Protection</li>
      <li>Anti-Exploit Protection</li>
      <li>LedgerPro Protection</li>
    </ul>
    <ul class="tick-list">
      <li>Event Monitoring</li>
      <li>Firewall</li>
      <li>Vulnerability Protection</li>
      <li>Web Reputation</li>
      <li>Browser Exploit Prevention</li>
      <li>Predictive Machine Learning</li>
      <li>Device Control</li>
      <li>Data Loss Prevention</li>
      <li>URL Filtering</li>
      <li>Application Control</li>
    </ul>
  </div>
  <div class="abs contact">
    <div class="contact-phone">
      <svg width="26" height="26" viewBox="0 0 26 26" aria-hidden="true">
        <circle cx="13" cy="13" r="13" fill="var(--yellow)"/>
        <path d="M9 7 l3 3 -1.6 1.8 c1 2 2.2 3.2 4 4 l1.8-1.6 3 3 -1.8 1.8 c-5 -0.5 -9.5 -5 -10 -10 Z" fill="var(--black)"/>
      </svg>
      (555) 314-2968
    </div>
    <div class="contact-email">Sales@bytharo-example.com</div>
  </div>
  <div class="abs brand-name back-brand">Bytharo</div>
</section>

</body>
</html>
```